Website for Painting Company

Hi,
We are after a Wordpress website design with CSS/HTML Theme for our painting company based in Brisbane, Australia. Our business name is Bevan Molloy Painting Contractors and we have been trading for 33 years.
We want a website that is modern and fresh with a professional image. Our organisation does Commercial, Residential and Insurance Painting projects. I have listed a couple of similar websites that we like the look and feel of. These are a guide only and we are happy to see you own designs with a similar professional image.
http://www.kelvardpainters.com.au/
http://www.unitedcoatworks.com.au/
We are a member of Guild Decorator Australia and I have supplied the logo named "gda" which I have included in the files I have uploaded.
We want a five page site. These are Home Page, Residential, Commercial, Insurance and Contact Us.
I have also uploaded our logo and some pictures labeled Logo,Residential, Commercial, Insurance and Homepage. These should be used on each page listed above.
Updates
Project Deadline Extended
Reason: We are extending because we need more time to go through the designs and give feedback. There are many fantastic designs. Thank you everyone who has contributed!!!!
All the best
Derek
Industry/Entity Type
Painting
Requirements
Must have
- We want a five page site. These are Home Page, Residential, Commercial, Insurance and Contact Us.

```html
<!DOCTYPE html>
<html lang="en">
<head>
<meta charset="utf-8">
<title>Bevan Molloy Painting Contractors</title>
<link href="https://fonts.googleapis.com/css2?family=Archivo+Black&family=Roboto:wght@300;400;700&display=swap" rel="stylesheet">
<style>
:root{
  --red:#ee1c24;
  --red-dark:#c8101a;
  --yellow:#ffc629;
  --ink:#111;
  --grey-text:#555;
  --slogan:#a8a8a8;
  --bg-bottom:#a9a9a9;
}
*{margin:0;padding:0;box-sizing:border-box}
html,body{width:1129px;height:1200px;overflow:hidden}
body{position:relative;background:linear-gradient(180deg,#f4f4f4 0,#dadada 300px,var(--bg-bottom) 1100px);font-family:Roboto,Arial,sans-serif;color:var(--grey-text)}
.abs{position:absolute}
.brand-name{left:97px;top:38px;font-family:"Archivo Black",Arial,sans-serif;font-size:56px;letter-spacing:-2px;color:var(--ink);line-height:1}
.brand-ribbon{left:99px;top:104px;width:418px;height:34px}
.brand-tag{left:99px;top:104px;width:372px;height:34px;text-align:center;font:700 22px/34px Roboto,Arial,sans-serif;color:var(--yellow);letter-spacing:-.5px}
.call-badge{left:850px;top:0;width:170px;height:162px}
.call-name{left:860px;top:50px;width:150px;text-align:center;font:700 12px/1.2 Roboto,Arial,sans-serif;color:var(--red)}
.call-label{left:850px;top:95px;width:170px;text-align:center;font:700 13px Roboto,Arial,sans-serif;color:#fff}
.call-phone{left:850px;top:113px;width:170px;text-align:center;font:700 20px Roboto,Arial,sans-serif;color:var(--ink);letter-spacing:-.5px}
.red-band{left:47px;top:462px;width:1036px;height:122px;background:linear-gradient(180deg,var(--red),var(--red-dark));border-radius:8px 8px 0 0}
.slider{left:99px;top:139px;width:931px;height:396px;background:#fff;border:1px solid #ddd;box-shadow:0 6px 10px rgba(0,0,0,.25)}
.slider-brush{left:99px;top:140px;width:258px;height:150px;background:radial-gradient(ellipse at 70% 55%,#f3c200 0,#e8a94a 30%,#f6e7da 60%,#fff 80%)}
.slider-photo{left:355px;top:168px;width:660px;height:326px;background:linear-gradient(180deg,#e9e6e1 0,#cfc7bc 45%,#e6e4e0 70%,#cfcac4 100%);border-radius:18px;box-shadow:0 0 0 6px #efe0c8}
.slogan{left:107px;top:380px;font:700 27px/33px Roboto,Arial,sans-serif;color:var(--slogan);letter-spacing:-1px;text-shadow:1px 1px 0 #777}
.dots{left:655px;top:502px;display:flex;gap:8px}
.dots span{width:15px;height:15px;border-radius:50%;background:#f28c8c}
.dots span:first-child{background:#fde1a9}
.main-nav{left:230px;top:544px;display:flex;height:36px}
.main-nav a{font:700 18px/36px Roboto,Arial,sans-serif;color:var(--yellow);text-decoration:none;padding:0 25px;border-left:1px solid rgba(255,255,255,.25);letter-spacing:-.5px}
.main-nav a:first-child{border-left:none}
.content{left:47px;top:584px;width:1036px;height:510px;background:#fff}
.intro-title{left:99px;top:598px;width:560px;font:700 21px/25px Roboto,Arial,sans-serif;color:var(--red)}
.intro-text{left:99px;top:654px;width:557px;font:300 13px/16px Roboto,Arial,sans-serif;text-align:justify;color:#444}
.intro-text p{margin-bottom:16px}
.newsletter-title{left:99px;top:943px;font:700 42px Roboto,Arial,sans-serif;color:var(--red);letter-spacing:-2px}
.field{top:1000px;height:31px;background:var(--red);color:#fff;font:700 13px/31px Roboto,Arial,sans-serif;padding-left:8px;box-shadow:1px 2px 3px rgba(0,0,0,.3)}
.subscribe{left:565px;top:1000px;width:84px;height:31px;background:var(--yellow);color:var(--red);font:700 13px/31px Roboto,Arial,sans-serif;text-align:center;box-shadow:1px 2px 3px rgba(0,0,0,.3)}
.side-band{left:731px;width:228px;height:43px;background:linear-gradient(90deg,rgba(238,28,36,0) 0,var(--red) 22%,var(--red) 100%)}
.side-roller{left:959px;width:70px;height:43px;background:linear-gradient(180deg,#e6e6e6,#b9b9b9)}
.side-title{left:735px;width:198px;text-align:right;font:700 21px/43px Roboto,Arial,sans-serif;color:var(--yellow)}
.avatar{left:748px;top:677px;width:87px;height:98px;border:1px solid var(--red);background:linear-gradient(180deg,#d9dde2,#5d6b7c)}
.testimonial{left:748px;top:677px;width:270px;font:300 13px/16px Roboto,Arial,sans-serif;color:#444;text-align:justify}
.testimonial .wrap{float:left;width:92px;height:100px}
.badge{left:821px;top:918px;width:107px;height:97px;border:1px solid var(--red);background:#fff;padding:8px}
.badge div{width:100%;height:100%;background:linear-gradient(135deg,#d6dcf3,#f4d3d3)}
.badge-caption{left:760px;top:1024px;width:230px;text-align:center;font:400 13px Roboto,Arial,sans-serif;color:#444}
.footer{left:0;top:1086px;width:1129px;height:114px}
.foot-nav{left:143px;top:1140px;display:flex}
.foot-nav a{font:700 16px Roboto,Arial,sans-serif;color:#fff;text-decoration:none;margin-right:42px;letter-spacing:-.5px}
.foot-copy{right:111px;top:1107px;text-align:right;font:400 11px/13px Roboto,Arial,sans-serif;color:#fff}
.foot-addr{right:111px;top:1157px;text-align:right;font:400 11px/13px Roboto,Arial,sans-serif;color:#fff}
</style>
</head>
<body>

<header>
  <div class="abs brand-name">Bevan Molloy</div>
  <svg class="abs brand-ribbon" viewBox="0 0 418 34"><polygon points="0,0 372,0 372,8 418,8 404,21 418,34 0,34" fill="var(--red)"/><polygon points="372,8 395,8 372,0" fill="var(--red-dark)"/></svg>
  <div class="abs brand-tag">PAINTING CONTRACTORS</div>

  <svg class="abs call-badge" viewBox="0 0 170 162"><polygon points="0,0 170,0 170,140 85,162 0,140" fill="var(--yellow)"/></svg>
  <div class="abs call-name">Bevan Molloy<br>Painting Contractors</div>
  <div class="abs call-label">CALL US</div>
  <div class="abs call-phone">07-3555-0142</div>
</header>

<div class="abs red-band"></div>

<section class="abs slider" aria-label="Feature slider"></section>
<div class="abs slider-brush" role="img" aria-label="Hand holding a paintbrush dipped in a can of yellow paint"></div>
<div class="abs slider-photo" role="img" aria-label="Bright open-plan living and dining room with white tiled floor"></div>
<div class="abs slogan">HELP YOU<br>FIND THE RIGHT<br>COLOUR FOR YOUR<br>HOME INSIDE OUT</div>
<div class="abs dots"><span></span><span></span><span></span></div>

<nav class="abs main-nav">
  <a href="#">Home</a><a href="#">Residential</a><a href="#">Commercial</a><a href="#">Insurance</a><a href="#">Contact Us</a>
</nav>

<main class="abs content"></main>

<h1 class="abs intro-title">Bevan Molloy Contractors will help you find the right colour for your home, inside and out.</h1>
<div class="abs intro-text">
  <p>Bevan Molloy Contractors will help you find the right colour for your home, inside and out. We have a selection of residential options for interiors or exteriors. Whether you need a refreshing change for your bedroom, or to renew weather beaten surfaces outside, Bevan Molloy Contractors are the ones to look after your home.</p>
  <p>Bevan Molloy Contractors will help you find the right colour for your home, inside and out. We have a selection of residential options for interiors or exteriors. Whether you need a refreshing change for your bedroom, or to renew weather beaten surfaces outside, Bevan Molloy Contractors are the ones to look after your home. Bevan Molloy Contractors will help you find the right colour for your home, inside and out. We have a selection of residential options for interiors or exteriors. Whether you need a refreshing change for your bedroom, or to renew weather beaten surfaces outside, Bevan Molloy Contractors are the ones to look after your home.</p>
  <p>Bevan Molloy Contractors will help you find the right colour for your home, inside and out. We have a selection of residential options for interiors or exteriors. Whether you need a refreshing change for your bedroom, or to renew weather beaten surfaces outside,</p>
</div>

<h2 class="abs newsletter-title">Newsletter Signup !</h2>
<div class="abs field" style="left:99px;width:228px">Your Name</div>
<div class="abs field" style="left:335px;width:227px">Your Email</div>
<div class="abs subscribe">Subscribe</div>

<aside>
  <div class="abs side-band" style="top:614px"></div>
  <div class="abs side-roller" style="top:614px" role="img" aria-label="Paint roller resting at the end of the heading"></div>
  <div class="abs side-title" style="top:614px">Testimonials</div>
  <div class="abs avatar" role="img" aria-label="Portrait of a client"></div>
  <div class="abs testimonial"><span class="wrap"></span>Bevan Molloy Contractors will help you find the right colour for your home, inside and out. We have a selection of residential options for interiors or exteri- Bevan Molloy Contractors will help you find the right colour for your home, inside and out. We have a selection of residential options for interiors or exteriors. Whether</div>

  <div class="abs side-band" style="top:857px"></div>
  <div class="abs side-roller" style="top:857px" role="img" aria-label="Paint roller resting at the end of the heading"></div>
  <div class="abs side-title" style="top:857px;left:742px">Membership</div>
  <div class="abs badge" role="img" aria-label="Membership badge"><div></div></div>
  <div class="abs badge-caption">Guild Decorator Australia</div>
</aside>

<footer>
  <svg class="abs footer" viewBox="0 0 1129 114" preserveAspectRatio="none"><path d="M0,18 C40,10 80,22 130,14 C200,6 260,20 330,12 C420,4 500,20 600,12 C700,6 780,18 860,10 C940,4 1020,16 1070,8 L1129,12 L1129,114 L0,114Z" fill="var(--red)"/></svg>
  <nav class="abs foot-nav"><a href="#">Home</a><a href="#">Residential</a><a href="#">Commercial</a><a href="#">Insurance</a><a href="#">Contact Us</a></nav>
  <div class="abs foot-copy">© 2012 Bevan Molloy Painting Contractors.<br>All Rights Reserved.</div>
  <div class="abs foot-addr">42 Wattle St, Brisbane, QLD 4000<br>P. 07-3555-0142 &nbsp;&nbsp;&nbsp;&nbsp; | F. 07-3555-0143</div>
</footer>

</body>
</html>
```